Letterhead design for VELMORA company

I need an A4 letterhead design for my company "Velmora Household Wares". I need the letterhead to match my current logo and business card designs. I would like it to be colourful and match the design of the business card in terms of the flowing line of colour where the information is.  

Target Market(s)

Adults aged 20 - 50 Upper middle class.

Industry/Entity Type

It Company

Requirements
Must have
• Must be A4 size and match my current logo and business card designs. Must be clean simple and eye catching.

• Must have the following information

• Velmora Household Wares LTD
• 7 Harbeck Row
• Chiswick
• London
• England
• W7 2RZ
• Company No. 04521963
• VAT No. GB 371562048

• Telephone: 02079460318
• Mobile: 07700900412
• Email: info@velmora-wares.co.uk
Nice to have
• nice to have a wave of colour like the business card.
Should not have
• Should not be a different colour scheme to the business card and logo design.

```html
<!DOCTYPE html>
<html lang="en">
<head>
<meta charset="utf-8">
<title>Velmora Household Wares – Letterhead</title>
<link rel="stylesheet" href="https://fonts.googleapis.com/css2?family=Questrial&display=swap">
<style>
  :root {
    --teal: #1b8db0;
    --teal-dark: #0d6a88;
    --teal-light: #4cc6e6;
    --ink: #1a93b8;
    --paper: #ffffff;
    --backdrop: #eceff1;
  }
  * { margin: 0; padding: 0; box-sizing: border-box; }
  html, body {
    width: 1200px;
    height: 765px;
    overflow: hidden;
    background: var(--backdrop);
    font-family: "Questrial", "Century Gothic", sans-serif;
  }
  .letterhead {
    position: absolute;
    left: 342px;
    top: 20px;
    width: 516px;
    height: 725px;
    background: var(--paper);
    box-shadow: 0 2px 10px rgba(0,0,0,0.15);
    overflow: hidden;
  }
  .header-artwork {
    position: absolute;
    left: 0; top: 0;
    width: 205px; height: 100px;
    background: linear-gradient(135deg, #1a8cb0 0%, #33b4d9 50%, #0f7597 100%);
  }
  .header-brand {
    position: absolute;
    left: 209px; top: 0;
    width: 307px; height: 100px;
    background: linear-gradient(90deg, var(--teal) 0%, #1f9cc0 100%);
  }
  .brand-name, .brand-tagline {
    position: absolute;
    right: 34px;
    color: #ffffff;
    font-weight: 400;
    text-align: right;
    white-space: nowrap;
  }
  .brand-name {
    top: 22px;
    font-size: 40px;
    letter-spacing: 1px;
    line-height: 1;
  }
  .brand-tagline {
    top: 69px;
    font-size: 14px;
    letter-spacing: 0.5px;
  }
  .address {
    position: absolute;
    right: 37px;
    top: 111px;
    text-align: right;
    color: var(--ink);
    font-style: normal;
    font-size: 6.5px;
    letter-spacing: 1.6px;
    line-height: 11.8px;
  }
  .address .registration {
    font-size: 5px;
    letter-spacing: 1px;
    line-height: 8.5px;
    margin-top: 1px;
  }
  .contact {
    position: absolute;
    right: 37px;
    top: 662px;
    text-align: right;
    color: var(--ink);
    font-size: 8px;
    letter-spacing: 1.6px;
    line-height: 12.7px;
  }
  .contact .email { font-weight: 700; -webkit-text-stroke: 0.3px var(--ink); }
  .footer-band {
    position: absolute;
    left: 0; top: 706px;
    width: 516px; height: 19px;
    background: linear-gradient(90deg, var(--teal-dark) 0%, var(--teal) 25%, var(--teal-light) 55%, var(--teal) 80%, var(--teal-dark) 100%);
  }
  .footer-band::after {
    content: "";
    position: absolute;
    left: 0; right: 0; bottom: 5px;
    height: 2px;
    background: rgba(8, 70, 92, 0.55);
  }
</style>
</head>
<body>
  <main class="letterhead">
    <div class="header-artwork" role="img" aria-label="Decorative flowing wave artwork in blue tones"></div>

    <header class="header-brand">
      <div class="brand-name">VELMORA</div>
      <div class="brand-tagline">Velmora Household Wares</div>
    </header>

    <address class="address">
      <div>7 Harbeck Row</div>
      <div>Chiswick</div>
      <div>London</div>
      <div>England</div>
      <div>W7 2RZ</div>
      <div class="registration">Company No. 04521963<br>VAT No. GB 371562048</div>
    </address>

    <div class="contact">
      <div>p: 02079460318</div>
      <div>m: 07700900412</div>
      <div class="email">e: info@velmora-wares.co.uk</div>
    </div>

    <div class="footer-band"></div>
  </main>
</body>
</html>
```